Real Estate agent needs flyer/folder to contain bio and overview of services

I'm including files of the layout of the small folder. The folder is 6 1/2 across and 9 1/2 inches long. It will have a front & back cover and then writing on the 2 inside pages.

I am sending a few files to incorporate into the flyer, 1 new logo to use and 2 files which are coloring ideas.

```html
<!DOCTYPE html>
<html lang="en">
<head>
<meta charset="utf-8">
<title>Folder – cover &amp; cover back</title>
<link href="https://fonts.googleapis.com/css2?family=Merriweather:wght@300;400&family=Montserrat:wght@800&family=Open+Sans:wght@400&display=swap" rel="stylesheet">
<style>
  :root{
    --royal:#0314a0;
    --bright:#1438e0;
    --cyan:#00e8ff;
    --turquoise:#3de8c8;
    --stone:#9aa08a;
    --ink:#000;
    --paper:#fff;
    --icon-bg:#cfeff8;
    --icon-ink:#1a9ec0;
  }
  *{margin:0;padding:0;box-sizing:border-box}
  html,body{width:1200px;height:922px;overflow:hidden;background:var(--paper)}
  .sheet{position:relative;width:1200px;height:922px}
  .sheet-title{position:absolute;top:-6px;left:0;width:1120px;text-align:center;
    font:400 38px/1 "Merriweather",serif;color:var(--ink)}
  .artwork{position:absolute;left:0;top:0}
  .back-cover-text{position:absolute;left:395px;top:401px;width:158px;
    font:300 13px/18.2px "Merriweather",serif;color:var(--paper)}
  .brokerage-name{position:absolute;left:182px;top:452px;width:166px;text-align:center;
    font:400 19px/1.25 "Open Sans",sans-serif;color:var(--royal)}
  .contact{position:absolute;left:310px;top:728px;color:var(--paper);font-family:"Open Sans",sans-serif}
  .contact-name{font-size:26px;margin-left:23px;margin-bottom:10px}
  .contact-line{display:flex;align-items:center;gap:8px;font-size:20px;height:31px}
  .contact-line svg{width:15px;height:15px;flex:none}
  .faint-name{position:absolute;left:58px;top:790px;width:180px;text-align:center;
    font:400 22px/1 "Merriweather",serif;color:#1a2ab8;opacity:.6}
  .agent-name{position:absolute;left:630px;top:466px;width:290px;text-align:center}
  .agent-name-text{font:400 30px/1 "Merriweather",serif;color:var(--bright)}
  .agent-name-title{font:400 10px/1 "Merriweather",serif;color:var(--ink);margin-top:10px;letter-spacing:.5px}
  .tagline{position:absolute;left:968px;top:436px;color:var(--paper)}
  .tagline-lead{font:400 20px/1 "Merriweather",serif}
  .tagline-you{font:800 86px/1 "Montserrat",sans-serif;letter-spacing:-2px;margin-top:2px}
  .tagline-you .t{color:var(--turquoise)}
  .tagline-you .s{color:var(--stone)}
</style>
</head>
<body>
<div class="sheet">
  <h1 class="sheet-title">cover &amp; cover back</h1>

  <svg class="artwork" width="1200" height="922" viewBox="0 0 1200 922">
    <defs>
      <clipPath id="front-cover-shape">
        <path d="M600 45 H1060 A832 832 0 0 1 1060 922 H600 Z"/>
      </clipPath>
      <linearGradient id="silver-band" x1="0" y1="0" x2="1" y2="0.6">
        <stop offset="0" stop-color="#f4f4f4"/>
        <stop offset=".45" stop-color="#e2e2e2"/>
        <stop offset=".75" stop-color="#a8a8a8"/>
        <stop offset="1" stop-color="#eeeeee"/>
      </linearGradient>
      <linearGradient id="cyan-wedge" x1="0" y1="0" x2="1" y2="1">
        <stop offset="0" stop-color="#1a7cff"/>
        <stop offset="1" stop-color="var(--cyan)"/>
      </linearGradient>
      <linearGradient id="towers-fade" x1="0" y1="0" x2="0" y2="1">
        <stop offset="0" stop-color="#fff"/>
        <stop offset="1" stop-color="#e6e6e6"/>
      </linearGradient>
      <linearGradient id="marina-photo" x1="0" y1="0" x2="1" y2="1">
        <stop offset="0" stop-color="#2a55d8"/>
        <stop offset=".6" stop-color="#1a3ee6"/>
        <stop offset="1" stop-color="#0a2ad0"/>
      </linearGradient>
      <linearGradient id="city-haze" x1="0" y1="0" x2="1" y2="0">
        <stop offset="0" stop-color="#1a55b0" stop-opacity=".75"/>
        <stop offset="1" stop-color="#1a55b0" stop-opacity=".35"/>
      </linearGradient>
    </defs>

    <!-- back cover -->
    <rect class="back-cover" x="0" y="45" width="600" height="877" fill="var(--royal)"/>
    <path class="city-haze" d="M0 262 H78 Q92 262 104 274 L230 392 Q250 408 268 410 L268 560 Q150 570 100 640 L0 700 Z"
          fill="url(#city-haze)" role="img" aria-label="Faint city skyline behind the brokerage badge"/>
    <circle cx="265" cy="484" r="94" fill="#d8d8d8"/>
    <circle cx="265" cy="484" r="88" fill="var(--paper)"/>

    <!-- front cover -->
    <g clip-path="url(#front-cover-shape)">
      <rect x="600" y="45" width="600" height="877" fill="var(--paper)"/>
      <polygon points="600,45 1060,45 600,305" fill="url(#silver-band)"
               role="img" aria-label="Silver band with a pixel skyline"/>
      <polygon points="600,45 618,45 672,176 600,215" fill="url(#cyan-wedge)"/>
      <rect x="600" y="630" width="600" height="292" fill="url(#towers-fade)"
            role="img" aria-label="Pale high-rise towers rising from the bottom edge"/>
      <path d="M1013 342 H1200 V625 H1073 Q933 625 933 485 V422 Q933 342 1013 342 Z"
            fill="url(#marina-photo)" role="img" aria-label="Blue-toned photo of a community entrance sign"/>
    </g>
    <path d="M600 45 H1060 A832 832 0 0 1 1060 922" fill="none" stroke="var(--ink)" stroke-width="1"/>
    <line x1="0" y1="45" x2="600" y2="45" stroke="var(--ink)" stroke-width="1"/>
  </svg>

  <p class="back-cover-text">Along with being your Realtor, I'm a lifelong resource for all things home-related &amp; beyond...if you need a great referral for anything at all, call me! I can't wait to work with you!</p>

  <div class="brokerage-name">Summit Realty Group</div>

  <div class="faint-name">Clara Montrose</div>

  <div class="contact">
    <div class="contact-name">Clara Montrose</div>
    <div class="contact-line">
      <svg viewBox="0 0 16 16"><rect width="16" height="16" fill="var(--icon-bg)"/><path d="M4 3l2 0 1 3-1.5 1a7 7 0 0 0 3.5 3.5l1-1.5 3 1v2c0 1-1 1.5-2 1.3C6.5 12.5 3.5 9.5 2.7 5 2.5 4 3 3 4 3z" fill="var(--icon-ink)"/></svg>
      <span>555 013 4827</span>
    </div>
    <div class="contact-line">
      <svg viewBox="0 0 16 16"><rect width="16" height="16" fill="var(--icon-bg)"/><rect x="2" y="4" width="12" height="8" fill="none" stroke="var(--icon-ink)"/><path d="M2 4l6 5 6-5" fill="none" stroke="var(--icon-ink)"/></svg>
      <span>clara@claramhomes.com</span>
    </div>
    <div class="contact-line">
      <svg viewBox="0 0 16 16"><rect width="16" height="16" fill="var(--icon-bg)"/><circle cx="8" cy="8" r="5.5" fill="none" stroke="var(--icon-ink)"/><path d="M2.5 8h11M8 2.5c-3 3-3 8 0 11M8 2.5c3 3 3 8 0 11" fill="none" stroke="var(--icon-ink)"/></svg>
      <span>www.claramhomes.com</span>
    </div>
  </div>

  <div class="agent-name">
    <div class="agent-name-text">Clara Montrose</div>
    <div class="agent-name-title">REALTOR®</div>
  </div>

  <div class="tagline">
    <div class="tagline-lead">It's all about</div>
    <div class="tagline-you"><span class="t">Y</span><span class="s">O</span><span class="t">U</span></div>
  </div>
</div>
</body>
</html>
```